File Download Website

We are looking for a design for a file download website. Our objective is to allow users to upload/browse/download files. This means we need 3 different pages.
The upload page should allow users to upload a file, we are looking for creative designs, a file box with a browse button next to it is already out there so the design must bring something new.
The browse page should display a users files/folders.
The download page should allow the user to download a file.
We do not require any code, only design. The designer is given complete freedom over the design, you may go about it however you like. This is a test of creativity, whoever this project goes to will definitely be given more work in the near future.
Example of a well designed file download website: cloudvane.net
Target Market(s)
15-30 year old people
Industry/Entity Type
Work
Look and feel
Each slider illustrates characteristics of the customer's brand and the style your logo design should communicate.

```html
<!DOCTYPE html>
<html lang="en">
<head>
<meta charset="utf-8">
<title>Sharevale – File Sharing</title>
<link href="https://fonts.googleapis.com/css2?family=Arimo:wght@400;700&display=swap" rel="stylesheet">
<style>
:root{
  --topbar:#0b3f5c;
  --blue-dark:#0e6a9c;
  --blue:#1585bd;
  --blue-light:#2ba0d6;
  --orange:#f7941d;
  --orange-dark:#e0700a;
  --page-grey:#ececec;
  --card:#ffffff;
  --tile:#f3f3f3;
  --tile-border:#cfcfcf;
  --ink:#333333;
  --ink-soft:#555555;
  --link-blue:#1a7fc0;
  --footer:#2b2b2b;
  --footer-bottom:#1b1b1b;
  --white:#ffffff;
}
*{box-sizing:border-box;margin:0;padding:0}
html,body{width:1200px;height:1072px;overflow:hidden}
body{position:relative;background:var(--page-grey);font-family:"Arimo",Arial,sans-serif;color:var(--ink)}
.abs{position:absolute}

/* top bar */
.top-bar{left:0;top:0;width:1200px;height:31px;background:linear-gradient(var(--topbar),#0f4d70)}
.account-links{right:0;top:0;height:31px;display:flex;gap:22px;align-items:center;padding-right:188px;font-size:11px;color:var(--white)}

/* search band */
.search-band{left:0;top:31px;width:1200px;height:71px;background:linear-gradient(90deg,#0e6ea3,#2a9fd6 50%,#0e6ea3);border-bottom:1px solid #0c5c88}
.search-input{left:339px;top:41px;width:418px;height:32px;background:var(--white);border:2px solid #d5e6f0;border-radius:5px;box-shadow:inset 0 2px 3px rgba(0,0,0,.2)}
.search-button{left:767px;top:41px;width:99px;height:32px;background:linear-gradient(var(--orange),var(--orange-dark));border-radius:4px;color:var(--white);font-size:19px;display:flex;align-items:center;justify-content:center;box-shadow:0 1px 2px rgba(0,0,0,.3)}
.category-links{top:81px;font-size:10px;color:var(--white);transform:translateX(-50%)}

/* hero */
.hero{left:0;top:102px;width:1200px;height:357px;background:linear-gradient(90deg,#0d6494,#1688c0 50%,#0d6494)}
.brand{left:169px;top:146px;font-size:62px;font-weight:700;color:var(--white);letter-spacing:-1px}
.main-nav{left:590px;top:186px;width:449px;height:41px;background:linear-gradient(#ffffff,#e2e2e2);border-radius:5px;display:flex;box-shadow:0 8px 10px -4px rgba(0,0,0,.4)}
.main-nav span{display:flex;align-items:center;justify-content:center;font-size:13px;color:#222;border-right:1px solid #c8c8c8}
.main-nav span:last-child{border-right:none}

.upload-panel{left:162px;top:258px;width:564px;height:293px;background:var(--white);border:1px solid #d0d0d0;border-radius:4px;box-shadow:0 12px 14px -8px rgba(0,0,0,.35)}
.drop-area{left:142px;top:10px;width:412px;height:273px;background:linear-gradient(#ffffff,#e6e6e6);border:1px solid #d6d6d6;box-shadow:inset 0 0 18px rgba(0,0,0,.12)}
.presenter-photo{left:0;top:0;width:142px;height:292px;background:linear-gradient(160deg,#e8dcd3,#3a3a3a 70%,#222);border-radius:4px 0 0 4px}
.upload-cta{left:173px;top:81px;width:358px;height:97px;background:linear-gradient(var(--blue-light),var(--blue-dark));border:1px solid #0c5f8d;border-radius:3px;color:var(--white);text-align:center;padding-top:14px}
.upload-cta .lead{font-size:20px}
.upload-cta .strong{font-size:31px;font-weight:700;margin-top:2px}

.register-label{left:774px;top:265px;font-size:15px;color:var(--white)}
.field{left:767px;width:240px;height:36px;background:linear-gradient(#f4f4f4,#ffffff);border:2px solid #0b5b86;border-radius:5px;font-size:15px;color:#555;padding:8px 12px;box-shadow:0 0 0 1px #7fc0e2}
.register-button{left:767px;top:484px;width:240px;height:37px;background:linear-gradient(var(--orange),var(--orange-dark));border:1px solid #c86508;color:var(--white);font-size:15px;display:flex;align-items:center;justify-content:center}

/* content */
.content-card{left:162px;top:583px;width:877px;height:366px;background:var(--card);border-radius:4px}
.feature-tile{top:611px;width:276px;height:190px;background:var(--tile);border:1px solid var(--tile-border);border-radius:3px}
.feature-button{left:33px;top:42px;width:200px;height:56px;background:linear-gradient(#2aa0d6,#0e6a9c);border:2px solid #9dc9e2;border-radius:5px;color:var(--white);padding:7px 14px;box-shadow:0 2px 3px rgba(0,0,0,.3)}
.feature-button .title{font-size:22px;font-weight:700;line-height:1}
.feature-button .title.long{font-size:19px;line-height:22px;margin-top:0}
.feature-button .sub{font-size:12px;font-weight:700;margin-top:3px}
.feature-button svg{position:absolute;right:14px;top:9px}
.feature-text{left:24px;top:120px;width:240px;font-size:11px;line-height:13px;color:var(--ink)}
.welcome-title{left:186px;top:821px;font-size:22px;font-weight:400;color:#222}
.welcome-title em{font-style:normal;color:var(--link-blue)}
.welcome-text{left:186px;top:855px;width:830px;font-size:11px;line-height:13.5px;color:var(--ink)}

/* footer */
.footer{left:0;top:960px;width:1200px;height:86px;background:var(--footer)}
.footer-links{left:0;top:14px;width:1200px;display:flex;justify-content:center;gap:14px;font-size:12px;color:var(--white)}
.follow{left:473px;top:52px;font-size:12px;color:var(--white)}
.copyright-bar{left:0;top:1046px;width:1200px;height:26px;background:var(--footer-bottom);color:var(--white);font-size:10px;display:flex;align-items:center;justify-content:center}
</style>
</head>
<body>
  <header>
    <div class="abs top-bar"></div>
    <div class="abs account-links"><span>Login</span><span>Sign Up</span></div>

    <div class="abs search-band"></div>
    <div class="abs search-input"></div>
    <div class="abs search-button">Find It</div>
    <span class="abs category-links" style="left:373px">File</span>
    <span class="abs category-links" style="left:424px">Video</span>
    <span class="abs category-links" style="left:479px">Music</span>
    <span class="abs category-links" style="left:534px">Photo</span>
    <span class="abs category-links" style="left:587px">Book</span>
    <span class="abs category-links" style="left:645px">Games</span>
    <span class="abs category-links" style="left:709px">Archives</span>
  </header>

  <section>
    <div class="abs hero"></div>
    <div class="abs brand">Sharevale</div>
    <nav class="abs main-nav">
      <span style="width:100px">UPLOAD</span>
      <span style="width:96px">PREMIUM</span>
      <span style="width:91px">TOOLS</span>
      <span style="width:85px">SIGN UP</span>
      <span style="width:77px">HELP</span>
    </nav>

    <div class="abs upload-panel">
      <div class="abs drop-area"></div>
      <div class="abs presenter-photo" role="img" aria-label="Photo of a smiling businesswoman pointing at the upload area"></div>
      <div class="abs upload-cta">
        <div class="lead">Drag &amp; Put Your Files Here</div>
        <div class="strong">UPLOAD NOW</div>
      </div>
    </div>

    <div class="abs register-label">Or start register through this form &nbsp;:</div>
    <div class="abs field" style="top:294px">Email</div>
    <div class="abs field" style="top:342px">Password</div>
    <div class="abs field" style="top:390px">Password Confirmation</div>
    <div class="abs register-button">REGISTER NOW</div>
  </section>

  <main>
    <div class="abs content-card"></div>

    <div class="abs feature-tile" style="left:174px">
      <div class="abs feature-button">
        <div class="title">UPLOAD</div><div class="sub">All of your files</div>
        <svg width="36" height="36" viewBox="0 0 40 38"><rect x="8" y="0" width="26" height="4" fill="#111"/><polygon points="20,9 37,23 28,23 28,36 12,36 12,23 3,23" fill="#fff"/></svg>
      </div>
      <p class="abs feature-text">Lorem ipsum dolor sit amet, consecteteur adipiscing elit. set diem nonumy in convalis gravida neque.</p>
    </div>

    <div class="abs feature-tile" style="left:462px">
      <div class="abs feature-button">
        <div class="title">Share</div><div class="sub">To anyone</div>
        <svg width="36" height="36" viewBox="0 0 40 38"><g stroke="#fff" stroke-width="2.5" fill="none"><line x1="20" y1="6" x2="20" y2="20"/><line x1="20" y1="20" x2="8" y2="31"/><line x1="20" y1="20" x2="32" y2="31"/><line x1="20" y1="20" x2="20" y2="31"/></g><g fill="#fff"><circle cx="20" cy="6" r="4"/><circle cx="8" cy="32" r="4"/><circle cx="20" cy="32" r="4"/><circle cx="32" cy="32" r="4"/></g></svg>
      </div>
      <p class="abs feature-text">Lorem ipsum dolor sit amet, consecteteur adipiscing elit. set diem nonumy in convalis gravida neque.</p>
    </div>

    <div class="abs feature-tile" style="left:751px">
      <div class="abs feature-button" style="padding-left:12px">
        <div class="title long">DOWNLOAD</div><div class="sub">It's very easy</div>
        <svg width="36" height="36" viewBox="0 0 40 38"><rect x="8" y="0" width="26" height="4" fill="#111"/><polygon points="12,9 28,9 28,21 37,21 20,36 3,21 12,21" fill="#fff"/></svg>
      </div>
      <p class="abs feature-text" style="top:112px">Lorem ipsum dolor sit amet, consecteteur adipiscing elit. set diem nonumy in convalis gravida neque.</p>
    </div>

    <h1 class="abs welcome-title">Welcome to <em>Sharevale.com</em></h1>
    <p class="abs welcome-text">Lorem ipsum dolor sit amet, consectetuer adipiscing elit. set diem nonumy nibh euismod tincidunt ut laoreet dolor magna aliquam erat volutpat. ut wisl enim ad minim veniam. Nemo enim ipsam voluptatem quia voluptas sit aspermatur aut odit aut fugit, set quia consequ untur. Lorem ipsum dolor sit amet, consec teteur adipiscing elit. set diem nonumy nibh euismod tincidunt ut laoret dolor magna aliquam erat volutpat. ut wisl enim ad minim veniam. nemo enim ipsam volutpat atem quia volutpat sit aspermatur aut odit aut fugit, set wula cinsequuntur.</p>
  </main>

  <footer>
    <div class="abs footer">
      <div class="abs footer-links">
        <span>Upload</span><span>I</span><span>Premium</span><span>I</span><span>Tools</span><span>I</span><span>Sign Up</span><span>I</span><span>Help</span><span>I</span><span>Advertise</span><span>I</span><span>Contact Us</span><span>I</span><span>Privacy Policy</span><span>I</span><span>Terms &amp; conditions</span>
      </div>
      <div class="abs follow">FOLLOW US ON &nbsp;&nbsp;:</div>
    </div>
    <div class="abs copyright-bar">Copyright &nbsp;©&nbsp; 20013. Sharevale.com. All rights reserved.</div>
  </footer>
</body>
</html>
```